Website for Clearway Living business

We need a website to present our video, audio and print content to subcribers at Vivid Horizon Mentors. We will offer a team of coaches who can help people breakthrough the barriers that keep them from reaching their physical, spiritual, financial, leadership and relationship goals.

Target Market(s)

Anyone who needs help with strategies to take their life to a new level of success.

Industry/Entity Type

Life Coaching

Logo Text

Vivid Horizon Mentors

Number of Pages Required

5+ page

Colors

Designer to choose colors to be used in the design.

Requirements
Must have
• The ability to present content as a package that includes Word Documents, videos and audio content as well as to be able to display books for sale. Each week their would be a new package for subscribers to access. It should provide the ability for subscribers to comment on the material and share how their lives were changed by the content. Should also include a shop page to offer merchandise for sale.
Nice to have
• Not sure
Should not have
• Not sure

```html
<!DOCTYPE html>
<html lang="en">
<head>
<meta charset="utf-8">
<title>Clearway Living — Vivid Horizon Mentors</title>
<link rel="stylesheet" href="https://fonts.googleapis.com/css2?family=Roboto:wght@300;400;500;700&family=Hind:wght@400;500&display=swap">
<style>
:root{
  --blue:#0b56b2;
  --blue-deep:#0a4a9c;
  --orange:#f47e20;
  --ink:#2a2a2a;
  --text:#666;
  --muted:#9a9a9a;
  --card:#f1f1f1;
  --line:#e6e6e6;
  --footer:#2b2b2b;
  --footer-text:#8c6a4f;
  --white:#fff;
}
*{box-sizing:border-box;margin:0;padding:0}
html,body{width:1200px;height:3285px;overflow:hidden}
body{position:relative;background:var(--white);font-family:"Roboto",Arial,sans-serif;color:var(--text)}
.heading{font-family:"Hind","Roboto",sans-serif;font-weight:500;color:var(--ink);font-size:23px;text-align:center}

/* header */
.site-header{position:absolute;left:0;top:0;width:1200px;height:88px;background:var(--white);z-index:2}
.brand{position:absolute;left:110px;top:16px}
.brand-name{font-family:"Roboto",sans-serif;font-size:26px;font-weight:400;color:var(--blue);line-height:1}
.brand-tag{font-size:12px;color:var(--orange);margin-top:4px}
.main-nav{position:absolute;left:442px;top:30px;display:flex;gap:26px;font-size:14px;color:#333}
.main-nav .active{padding-bottom:6px;border-bottom:2px solid var(--orange)}
.search{position:absolute;left:1076px;top:30px}

/* hero */
.hero{position:absolute;left:0;top:88px;width:1200px;height:508px;background:linear-gradient(90deg,#fbf3ea 0%,#f6ebe0 45%,#e9dccf 62%,#c9b5a6 75%,#8fa9bf 100%)}
.hero-copy{position:absolute;left:180px;top:96px;width:420px;text-align:center}
.hero-title{font-family:"Hind",sans-serif;font-weight:500;font-size:23px;color:#222}
.hero-quote{margin-top:18px;font-size:13.5px;line-height:24px;color:#5a4a3f}
.q{color:var(--orange);font-weight:700;font-size:16px}
.btn-primary{display:inline-block;margin-top:18px;background:var(--blue);color:var(--white);font-size:13px;font-weight:500;padding:11px 26px;border-radius:20px}

/* partner strip */
.partners{position:absolute;left:0;top:596px;width:1200px;height:98px;display:flex;justify-content:center;gap:80px;align-items:center}
.partner-badge{width:88px;height:34px;border-radius:6px;background:#d4d4d4}

/* signup band */
.signup{position:absolute;left:0;width:1200px;height:88px;background:var(--orange)}
.signup-text{position:absolute;left:175px;top:29px;font-family:"Hind",sans-serif;font-size:22px;color:var(--white)}
.signup-input{position:absolute;left:580px;top:24px;width:300px;height:40px;background:var(--white);border-radius:20px;font-size:12px;color:#888;padding:13px 18px}
.signup-btn{position:absolute;left:887px;top:24px;width:133px;height:40px;background:var(--blue);border-radius:20px;color:var(--white);font-size:13px;font-weight:700;text-align:center;line-height:40px}

/* services */
.services-title{position:absolute;left:0;top:870px;width:1200px}
.services-lead{position:absolute;left:260px;top:912px;width:680px;text-align:center;font-size:12.5px;line-height:21px}
.service{position:absolute;top:1012px;width:306px;text-align:center}
.service-photo{height:203px;border-radius:6px}
.service-name{margin-top:20px;font-size:15px;color:#333}
.service-text{margin-top:10px;font-size:12.5px;line-height:21px}
.btn-ghost{display:inline-block;margin-top:12px;background:#cfcfcf;color:var(--white);font-size:10px;font-weight:700;padding:6px 26px;border-radius:12px}

/* resources */
.resources{position:absolute;left:0;top:1412px;width:1200px;height:570px;background:var(--blue)}
.resources .heading{color:var(--white);position:absolute;top:48px;width:1200px}
.resources-sub{position:absolute;top:82px;width:1200px;text-align:center;color:var(--white);font-size:14px;font-weight:700}
.video-col{position:absolute;top:146px;width:300px;color:#d7e4f5}
.video-col h3{font-size:15px;color:var(--white);font-weight:700;margin-bottom:10px}
.video-col p{font-size:12.5px;line-height:21px}
.divider-v{position:absolute;top:150px;width:1px;height:100px;background:rgba(255,255,255,.3)}
.perks{position:absolute;left:112px;top:290px;color:var(--white)}
.perks h3{font-size:15px;font-weight:700;margin-bottom:14px}
.perks li{list-style:none;font-size:12.5px;line-height:24px;color:#e3ecf8;display:flex;align-items:center;gap:8px}
.video-player{position:absolute;left:526px;top:302px;width:500px;height:312px;border-radius:10px;background:linear-gradient(180deg,#3a3330,#1b1816 70%,#c9c9c9 92%,#e8e8e8);z-index:1}
.fade-band{position:absolute;left:0;top:1982px;width:1200px;height:60px;background:linear-gradient(#ececec,#fff)}

/* blog */
.blog-title{position:absolute;left:0;top:2104px;width:1200px}
.post{position:absolute;top:2168px;width:306px;height:267px;background:var(--card);padding:28px 26px}
.post::before{content:"";position:absolute;left:0;top:0;border-top:22px solid #444;border-right:22px solid transparent}
.post h4{font-size:15px;font-weight:500;color:#333;line-height:20px}
.post-date{font-size:10px;color:#999;margin-top:4px}
.post p{font-size:12px;line-height:20px;margin-top:16px}
.post-meta{position:absolute;left:26px;bottom:26px;right:26px;display:flex;align-items:center;font-size:11.5px}
.avatar{width:40px;height:40px;border-radius:50%;background:linear-gradient(#d8c3b0,#8b7260);margin-right:10px}
.author{color:var(--orange);font-weight:700;margin-left:4px}
.comments{margin-left:auto;display:flex;align-items:center;gap:4px}
.rule{position:absolute;left:0;top:2490px;width:1200px;height:1px;background:var(--line)}

/* reviews */
.reviews-title{position:absolute;left:0;top:2535px;width:1200px}
.review-grid{position:absolute;left:112px;top:2610px;width:518px;display:grid;grid-template-columns:repeat(4,126px);grid-auto-rows:126px;gap:4px}
.review-photo{background:linear-gradient(#e6e9ec,#b9c0c8)}
.view-all{background:#eef3f6;display:flex;align-items:center;justify-content:center;font-size:12px;color:#666}
.review-quote{position:absolute;left:680px;top:2660px;width:420px;text-align:center;font-size:13.5px;line-height:23px;color:#555}
.review-name{margin-top:16px;font-size:15px;color:#333}

/* footer */
.site-footer{position:absolute;left:0;top:3007px;width:1200px;height:278px;background:var(--footer)}
.foot-col{position:absolute;top:40px}
.foot-col h5{font-size:11px;font-weight:700;color:var(--white);margin-bottom:14px;letter-spacing:.3px}
.foot-col p{font-size:11.5px;line-height:19px;color:var(--footer-text)}
.social{display:flex;gap:8px}
.social span{width:32px;height:32px;border:1.5px solid #666;border-radius:50%}
.copyright{position:absolute;left:0;top:236px;width:1200px;text-align:center;font-size:11px;color:#666}
</style>
</head>
<body>

<header class="site-header">
  <div class="brand">
    <div class="brand-name">Clearway Living</div>
    <div class="brand-tag">Vivid Horizon Mentors</div>
  </div>
  <nav class="main-nav">
    <span class="active">Home</span><span>About</span><span>Work With Me</span><span>Blog</span><span>Free Stuff</span><span>Contact</span><span>Shop</span>
  </nav>
  <svg class="search" width="14" height="14" viewBox="0 0 14 14"><circle cx="6" cy="6" r="4.5" fill="none" stroke="#f47e20" stroke-width="1.6"/><line x1="9.3" y1="9.3" x2="13" y2="13" stroke="#f47e20" stroke-width="1.6"/></svg>
</header>

<section class="hero" role="img" aria-label="Smiling woman by a sunlit window">
  <div class="hero-copy">
    <h1 class="hero-title">Vivid Horizon Mentors</h1>
    <p class="hero-quote"><span class="q">“</span> Nullam ac urna eu felis dapibus condimentum sit amet a augue. Sed non neque elit. Sed ut imperdiet nisi. Proin condimentum fermentum nunc. Etiam pharetra, erat sed fermentum feugiat, velit mauris egestas quam, ut aliquam quis neque. Suspendisse in orci enim. <span class="q">”</span></p>
    <span class="btn-primary">Get Started Today!</span>
  </div>
</section>

<section class="partners">
  <span class="partner-badge"></span><span class="partner-badge"></span><span class="partner-badge"></span><span class="partner-badge"></span><span class="partner-badge"></span><span class="partner-badge"></span>
</section>

<section class="signup" style="top:694px">
  <div class="signup-text">Yes please, I want the free resources</div>
  <div class="signup-input">Email Address</div>
  <div class="signup-btn">SUBSCRIBE</div>
</section>

<h2 class="heading services-title">Ready To Run Your Business Instead of It Running You?</h2>
<p class="services-lead">Mauris vitae erat consequat auctor eu in elit. Class aptent taciti sociosqu ad litora torquent per conubia nostra, per inceptos himenaeos. Mauris in erat justo. Nullam ac urna eu felis dapibus condimentum sit amet a augue. Sed non neque elit. Sed ut imperdiet nisi. Proin condimentum fermentum nunc. Etiam pharetra, erat sed fermentum feugiat.</p>

<article class="service" style="left:112px">
  <div class="service-photo" role="img" aria-label="Group meeting in a bright office" style="background:linear-gradient(135deg,#9fb2c4,#4e5f70)"></div>
  <h3 class="service-name">Foundation</h3>
  <p class="service-text">Etiam pharetra, erat sed fermentum feugiat, velit mauris egestas quam, ut aliquam massa nisl quis neque. Suspendisse in orci enim.</p>
  <span class="btn-ghost">READ MORE ▸</span>
</article>
<article class="service" style="left:447px">
  <div class="service-photo" role="img" aria-label="Hands stacking wooden blocks" style="background:linear-gradient(135deg,#e2c7a4,#8a6a4c)"></div>
  <h3 class="service-name">Development</h3>
  <p class="service-text">Etiam pharetra, erat sed fermentum feugiat, velit mauris egestas quam, ut aliquam massa nisl quis neque. Suspendisse in orci enim.</p>
  <span class="btn-ghost">READ MORE ▸</span>
</article>
<article class="service" style="left:780px">
  <div class="service-photo" role="img" aria-label="Hands placing jigsaw pieces on a rising arrow" style="background:linear-gradient(135deg,#3b4654,#1f2530)"></div>
  <h3 class="service-name">Growth</h3>
  <p class="service-text">Etiam pharetra, erat sed fermentum feugiat, velit mauris egestas quam, ut aliquam massa nisl quis neque. Suspendisse in orci enim.</p>
  <span class="btn-ghost">READ MORE ▸</span>
</article>

<section class="resources">
  <h2 class="heading">Free ‘Find your Vivid Horizon’ Resources</h2>
  <p class="resources-sub">Nullam ac urna eu felis dapibus condimentum sit amet a augue.</p>
  <div class="video-col" style="left:112px"><h3>Video 01</h3><p>Etiam pharetra, erat sed fermentum feugiat, velit mauris egestas quam, ut aliquam massa nisl quis neque. Suspendisse in orci enim.</p></div>
  <div class="divider-v" style="left:425px"></div>
  <div class="video-col" style="left:446px"><h3>Video 02</h3><p>Etiam pharetra, erat sed fermentum feugiat, velit mauris egestas quam, ut aliquam massa nisl quis neque. Suspendisse in orci enim.</p></div>
  <div class="divider-v" style="left:758px"></div>
  <div class="video-col" style="left:780px"><h3>Video 03</h3><p>Etiam pharetra, erat sed fermentum feugiat, velit mauris egestas quam, ut aliquam massa nisl quis neque. Suspendisse in orci enim.</p></div>
  <div class="perks">
    <h3>You'll get :</h3>
    <ul>
      <li><svg width="12" height="12" viewBox="0 0 12 12"><path d="M2 6l3 3 5-6" fill="none" stroke="#8fd3ff" stroke-width="2"/></svg>Nam iaculis eros sed ultricies aliquam.</li>
      <li><svg width="12" height="12" viewBox="0 0 12 12"><path d="M2 6l3 3 5-6" fill="none" stroke="#8fd3ff" stroke-width="2"/></svg>Cras vel nisi vitae eros pulvinar varius et sed magna.</li>
      <li><svg width="12" height="12" viewBox="0 0 12 12"><path d="M2 6l3 3 5-6" fill="none" stroke="#8fd3ff" stroke-width="2"/></svg>Praesent hendrerit est id hendrerit congue.</li>
      <li><svg width="12" height="12" viewBox="0 0 12 12"><path d="M2 6l3 3 5-6" fill="none" stroke="#8fd3ff" stroke-width="2"/></svg>Fusce congue dolor vitae imperdiet imperdiet.</li>
      <li><svg width="12" height="12" viewBox="0 0 12 12"><path d="M2 6l3 3 5-6" fill="none" stroke="#8fd3ff" stroke-width="2"/></svg>Nam iaculis eros sed ultricies aliquam.</li>
      <li><svg width="12" height="12" viewBox="0 0 12 12"><path d="M2 6l3 3 5-6" fill="none" stroke="#8fd3ff" stroke-width="2"/></svg>Cras vel nisi vitae eros pulvinar varius et sed magna.</li>
      <li><svg width="12" height="12" viewBox="0 0 12 12"><path d="M2 6l3 3 5-6" fill="none" stroke="#8fd3ff" stroke-width="2"/></svg>Praesent hendrerit est id hendrerit congue.</li>
      <li><svg width="12" height="12" viewBox="0 0 12 12"><path d="M2 6l3 3 5-6" fill="none" stroke="#8fd3ff" stroke-width="2"/></svg>Fusce congue dolor vitae imperdiet imperdiet.</li>
    </ul>
  </div>
  <div class="video-player" role="img" aria-label="Laptop showing the introduction video player"></div>
</section>
<div class="fade-band"></div>

<h2 class="heading blog-title">From The Blog Posts</h2>
<article class="post" style="left:112px">
  <h4>Awesome lorem ipsum dosis suite this is a fresh version.</h4>
  <div class="post-date">25 Apr 2017</div>
  <p>Proin condimentum fermentum nunc. Etiam pharetra, erat sed fermentum feugiat, velit mauris egestas quam, ut aliquam massa nisl quis neque.</p>
  <div class="post-meta"><span class="avatar" role="img" aria-label="Author portrait"></span>By <span class="author">Owen Marsh</span><span class="comments"><svg width="12" height="11" viewBox="0 0 12 11"><path d="M1 1h10v6H5l-3 3V7H1z" fill="#777"/></svg>20</span></div>
</article>
<article class="post" style="left:447px">
  <h4>Awesome lorem ipsum dosis suite this is a fresh version.</h4>
  <div class="post-date">25 Apr 2017</div>
  <p>Proin condimentum fermentum nunc. Etiam pharetra, erat sed fermentum feugiat, velit mauris egestas quam, ut aliquam massa nisl quis neque.</p>
  <div class="post-meta"><span class="avatar" role="img" aria-label="Author portrait"></span>By <span class="author">Owen Marsh</span><span class="comments"><svg width="12" height="11" viewBox="0 0 12 11"><path d="M1 1h10v6H5l-3 3V7H1z" fill="#777"/></svg>20</span></div>
</article>
<article class="post" style="left:780px">
  <h4>Awesome lorem ipsum dosis suite this is a fresh version.</h4>
  <div class="post-date">25 Apr 2017</div>
  <p>Proin condimentum fermentum nunc. Etiam pharetra, erat sed fermentum feugiat, velit mauris egestas quam, ut aliquam massa nisl quis neque.</p>
  <div class="post-meta"><span class="avatar" role="img" aria-label="Author portrait"></span>By <span class="author">Owen Marsh</span><span class="comments"><svg width="12" height="11" viewBox="0 0 12 11"><path d="M1 1h10v6H5l-3 3V7H1z" fill="#777"/></svg>20</span></div>
</article>
<div class="rule"></div>

<h2 class="heading reviews-title">Happy Customer Reviews</h2>
<div class="review-grid">
  <div class="review-photo" role="img" aria-label="Customer portrait"></div>
  <div class="review-photo" role="img" aria-label="Customer portrait" style="background:linear-gradient(#cfd6de,#6f7d8c)"></div>
  <div class="review-photo" role="img" aria-label="Customer portrait"></div>
  <div class="review-photo" role="img" aria-label="Customer portrait"></div>
  <div class="review-photo" role="img" aria-label="Customer portrait"></div>
  <div class="review-photo" role="img" aria-label="Customer portrait"></div>
  <div class="review-photo" role="img" aria-label="Customer portrait"></div>
  <div class="view-all">VIEW ALL</div>
</div>
<div class="review-quote">
  <span class="q">“</span> Nullam ac urna eu felis dapibus condimentum sit amet a augue. Sed non neque elit. Sed ut imperdiet nisi. Proin condimentum fermentum nunc. Etiam pharetra, erat sed fermentum feugiat, velit mauris egestas quam, ut aliquam quis neque. Suspendisse in orci enim. <span class="q">”</span>
  <div class="review-name">Peter Lane</div>
</div>

<section class="signup" style="top:2919px">
  <div class="signup-text">Yes please, I want the free resources</div>
  <div class="signup-input">Email Address</div>
  <div class="signup-btn">SUBSCRIBE</div>
</section>

<footer class="site-footer">
  <div class="foot-col" style="left:112px;width:370px">
    <h5>ABOUT US</h5>
    <p>Neque porro quisquam est, qui dolorem ipsum quia dolor sit amet, consectetur, adipisci velit, sed quia non numquam eius modi tempora incidunt ut labore et dolore magnam aliquam reprehenderit qui in ea voluptate velit esse quam nihil modi tempora incidunt ut labore et dolore magnam aliquam tempora incidunt ut labore molestiae consequatur.</p>
  </div>
  <div class="foot-col" style="left:613px">
    <h5>CONTACT INFO</h5>
    <p>Clearway Living<br>14 Larkfield Row,<br>Brookvale 40512</p>
    <p style="margin-top:12px">1800 555 0192<br>hello@clearwayliving.example</p>
  </div>
  <div class="foot-col" style="left:865px">
    <h5>STAY CONNECTED</h5>
    <div class="social"><span></span><span></span><span></span><span></span><span></span></div>
  </div>
  <div class="copyright">© 2017 Clearway Living. All Rights Reserved.</div>
</footer>

</body>
</html>
```